Pharma business needs a catalogue design

Morvax Ltd. is a fast-growing pharma production company, and we need a catalogue design for white label products (as in unbranded ones). We would only want to distribute the catalogue digitally. Attached to this brief is our current product list.

We are also looking to upgrade the look of our product list so this is where you can display your creativity. Feel free to change up the look as much as you like in order to make it look better. You can also make it as long as you wish.

Important: Often times, our customers want to put their logo directly on our product catalogue. You should, therefore, design the catalogue with this in mind and make it simple for us to be able to replace the logo with another one.

The final design should communicate unwavering quality and incredible attention to detail.

Should you have any questions, please do not hesitate to contact us. We understand that any creative process takes joint effort and mutual understanding.

Industry/Entity Type

Pharmaceutical

Font styles to use
Decorative
Script

Colors

Designer to choose colors to be used in the design.

Requirements
Must have
• What is required is to change the photos of each product with tubes/boxes/packaging that just says "your brand here".

```html
<!DOCTYPE html>
<html lang="en">
<head>
<meta charset="utf-8">
<title>Morvax Pharma – Product List 2019</title>
<link href="https://fonts.googleapis.com/css2?family=Montserrat:wght@400;600;700;800&family=Open+Sans:wght@400;600&display=swap" rel="stylesheet">
<style>
  :root{
    --blue:#1f56b3;
    --blue-dark:#153f8a;
    --blue-light:#3b7ad8;
    --sky-top:#5f9fe0;
    --sky-bottom:#cfe3f7;
    --white:#ffffff;
    --ink:#27324a;
    --muted:#6b778f;
    --line:#dbe3f0;
    --backdrop:#eef1f6;
  }
  *{box-sizing:border-box;margin:0;padding:0}
  html,body{width:739px;height:1200px;overflow:hidden}
  body{background:var(--backdrop);font-family:"Open Sans",Arial,sans-serif;color:var(--ink);position:relative}

  .page{position:absolute;width:340px;height:481px;background:var(--white);overflow:hidden;box-shadow:0 6px 18px rgba(20,40,90,.18)}
  .page > svg.shapes{position:absolute;inset:0;width:100%;height:100%}

  /* front cover */
  .cover-front{left:379px;top:40px}
  .cover-title{position:absolute;top:26px;right:28px;text-align:right;color:var(--white);font-family:"Montserrat",Arial,sans-serif}
  .cover-title .title-line{display:block;font-weight:700;font-size:22px;letter-spacing:2px}
  .cover-title .title-year{display:block;font-weight:800;font-size:40px;line-height:1;letter-spacing:1px}
  .cover-web{position:absolute;left:24px;bottom:14px;color:var(--white);font-size:9px;font-family:"Montserrat",Arial,sans-serif;font-weight:600;letter-spacing:.5px}

  .brand-seal{position:absolute;width:78px;height:78px;border-radius:50%;background:var(--white);border:3px solid var(--blue);display:flex;align-items:center;justify-content:center;text-align:center}
  .brand-name{font-family:"Montserrat",Arial,sans-serif;font-weight:700;font-size:12px;line-height:1.15;color:var(--blue)}
  .cover-front .brand-seal{right:24px;top:296px}

  /* back cover */
  .cover-back{left:20px;top:40px}
  .back-content{position:absolute;left:22px;right:22px;top:160px;color:var(--white)}
  .section-heading{font-family:"Montserrat",Arial,sans-serif;font-weight:700;font-size:13px;letter-spacing:1px;margin-bottom:6px}
  .about-text{font-size:8px;line-height:1.6;opacity:.95;width:240px}
  .partner-row{display:flex;gap:10px;margin:22px 0 26px}
  .partner-badge{width:52px;height:26px;border-radius:4px;background:var(--white)}
  .contact-list{list-style:none;font-size:8px;line-height:1}
  .contact-list li{display:flex;align-items:center;gap:8px;margin-bottom:9px}
  .contact-list svg{width:12px;height:12px;flex:none}
  .cover-back .brand-seal{right:20px;bottom:20px;border-color:var(--white)}

  /* inner spread */
  .spread{position:absolute;left:20px;top:600px;width:699px;height:481px;display:flex;box-shadow:0 6px 18px rgba(20,40,90,.18)}
  .spread .page{position:relative;box-shadow:none;width:349.5px;height:481px}
  .spread .page + .page{border-left:1px solid var(--line)}
  .spread-header{position:absolute;left:20px;right:16px;top:16px;font-family:"Montserrat",Arial,sans-serif;font-weight:700;font-size:9.5px;letter-spacing:.4px;color:var(--blue);white-space:nowrap}
  .spread-header::after{content:"";display:block;width:60px;height:3px;background:var(--blue);margin-top:5px}
  .page-footer{position:absolute;left:0;right:0;bottom:0;width:100%;height:44px}
  .footer-web{position:absolute;z-index:1;bottom:10px;color:var(--white);font-family:"Montserrat",Arial,sans-serif;font-weight:600;font-size:8px;line-height:1}
  .page-left .footer-web{left:20px}
  .page-right .footer-web{right:20px}

  .product-block{position:absolute;left:16px;right:16px;display:flex;gap:12px;align-items:flex-start}
  .pack-wrap{position:relative;flex:none}
  .pack{width:70px;height:92px;border-radius:50%;background:radial-gradient(circle at 50% 45%, #eaf2fc 0%, #b8d2f0 70%, #8fb4e4 100%);border:2px solid var(--blue-light)}
  .count-badge{position:absolute;left:-6px;bottom:-4px;width:24px;height:24px;border-radius:50%;background:var(--blue);color:var(--white);font-family:"Montserrat",Arial,sans-serif;font-weight:700;font-size:9px;display:flex;align-items:center;justify-content:center;border:2px solid var(--white)}
  .product-info{flex:1}
  .product-title{font-family:"Montserrat",Arial,sans-serif;font-weight:700;font-size:8.5px;color:var(--blue);border-bottom:1px solid var(--line);padding-bottom:4px;margin-bottom:4px}
  .product-table{width:100%;border-collapse:collapse;font-size:7px;color:var(--ink)}
  .product-table td{padding:2.5px 0;border-bottom:1px dotted var(--line)}
  .product-table td:last-child{text-align:right;color:var(--muted)}
</style>
</head>
<body>

  <!-- Back cover -->
  <section class="page cover-back">
    <svg class="shapes" viewBox="0 0 340 481" preserveAspectRatio="none">
      <defs>
        <linearGradient id="backSky" x1="0" y1="0" x2="0" y2="1">
          <stop offset="0" stop-color="#6aa8e6"/>
          <stop offset="1" stop-color="#d7e8f8"/>
        </linearGradient>
      </defs>
      <g role="img" aria-label="Photo of a bright blue sky">
        <path d="M0 0H340V128Q170 175 0 120Z" fill="url(#backSky)"/>
      </g>
      <path d="M0 120Q170 175 340 128V481H0Z" fill="var(--blue)"/>
      <path d="M0 132Q180 190 340 140" fill="none" stroke="var(--white)" stroke-width="3" opacity=".6"/>
      <path d="M0 400Q170 380 340 420V481H0Z" fill="var(--blue-dark)"/>
    </svg>
    <div class="back-content">
      <h2 class="section-heading">ABOUT US</h2>
      <p class="about-text">Morvax Ltd. produces quality white label pharmaceuticals with strict care at every stage. Our effervescent vitamins and minerals are made to trusted standards and ready for your own brand.</p>
      <div class="partner-row">
        <span class="partner-badge"></span>
        <span class="partner-badge"></span>
        <span class="partner-badge"></span>
        <span class="partner-badge"></span>
      </div>
      <h2 class="section-heading">CONTACT US</h2>
      <ul class="contact-list">
        <li><svg viewBox="0 0 12 12"><path d="M3 1l2 2-1 1.5a6 6 0 0 0 3.5 3.5L9 7l2 2-1.5 2A9 9 0 0 1 1 2.5Z" fill="var(--white)"/></svg>+1 555 0142 880</li>
        <li><svg viewBox="0 0 12 12"><path d="M6 0.5a4 4 0 0 1 4 4c0 3-4 7-4 7s-4-4-4-7a4 4 0 0 1 4-4Zm0 2.5a1.5 1.5 0 1 0 0 3 1.5 1.5 0 0 0 0-3Z" fill="var(--white)"/></svg>12 Harbour Road, Lakeside</li>
        <li><svg viewBox="0 0 12 12"><rect x="1" y="2.5" width="10" height="7" rx="1" fill="none" stroke="var(--white)"/><path d="M1 3l5 3.5L11 3" fill="none" stroke="var(--white)"/></svg>info@morvaxpharma.com</li>
        <li><svg viewBox="0 0 12 12"><circle cx="6" cy="6" r="5" fill="none" stroke="var(--white)"/><path d="M1 6h10M6 1c-2 3-2 7 0 10M6 1c2 3 2 7 0 10" fill="none" stroke="var(--white)" stroke-width=".8"/></svg>www.morvaxpharma.com</li>
      </ul>
    </div>
    <div class="brand-seal"><span class="brand-name">Morvax<br>Pharma</span></div>
  </section>

  <!-- Front cover -->
  <section class="page cover-front">
    <svg class="shapes" viewBox="0 0 340 481" preserveAspectRatio="none">
      <defs>
        <linearGradient id="frontPhoto" x1="0" y1="0" x2="0" y2="1">
          <stop offset="0" stop-color="#5f9fe0"/>
          <stop offset=".6" stop-color="#cfe3f7"/>
          <stop offset="1" stop-color="#a9c6e6"/>
        </linearGradient>
      </defs>
      <g role="img" aria-label="Photo of a smiling family of four outdoors under a blue sky">
        <path d="M0 0H340V300Q200 352 0 312Z" fill="url(#frontPhoto)"/>
      </g>
      <path d="M0 312Q200 352 340 300V320Q200 372 0 332Z" fill="var(--blue)"/>
      <path d="M0 440Q170 412 340 430V481H0Z" fill="var(--blue)"/>
    </svg>
    <h1 class="cover-title"><span class="title-line">PRODUCT LIST</span><span class="title-year">2019</span></h1>
    <div class="brand-seal"><span class="brand-name">Morvax<br>Pharma</span></div>
    <span class="cover-web">www.morvaxpharma.com</span>
  </section>

  <!-- Inner pages 1–2 -->
  <div class="spread">
    <section class="page page-left">
      <h2 class="spread-header">VITAMINS &amp; MINERALS – EFFERVESCENT PRODUCTS</h2>

      <article class="product-block" style="top:66px">
        <div class="pack-wrap"><div class="pack" role="img" aria-label="Effervescent tube packaging reading Your Brand Here"></div><span class="count-badge">20</span></div>
        <div class="product-info">
          <h3 class="product-title">01 VITAMIN C EFFERVESCENT</h3>
          <table class="product-table">
            <tr><td>Orange flavour</td><td>20 tablets</td></tr>
            <tr><td>Lemon flavour</td><td>20 tablets</td></tr>
            <tr><td>Berry flavour</td><td>10 tablets</td></tr>
            <tr><td>Lime flavour</td><td>10 tablets</td></tr>
          </table>
        </div>
      </article>

      <article class="product-block" style="top:236px">
        <div class="pack-wrap"><div class="pack" role="img" aria-label="Effervescent tube packaging reading Your Brand Here"></div><span class="count-badge">20</span></div>
        <div class="product-info">
          <h3 class="product-title">02 MULTIVITAMIN EFFERVESCENT</h3>
          <table class="product-table">
            <tr><td>Orange flavour</td><td>20 tablets</td></tr>
            <tr><td>Mango flavour</td><td>20 tablets</td></tr>
            <tr><td>Lemon flavour</td><td>10 tablets</td></tr>
            <tr><td>Grape flavour</td><td>10 tablets</td></tr>
          </table>
        </div>
      </article>

      <svg class="page-footer" viewBox="0 0 350 44" preserveAspectRatio="none"><path d="M0 14Q175 0 350 20V44H0Z" fill="var(--blue)"/></svg>
      <span class="footer-web">www.morvaxpharma.com</span>
    </section>

    <section class="page page-right">
      <article class="product-block" style="top:22px">
        <div class="pack-wrap"><div class="pack" role="img" aria-label="Effervescent tube packaging reading Your Brand Here"></div><span class="count-badge">20</span></div>
        <div class="product-info">
          <h3 class="product-title">03 CALCIUM + VITAMIN D</h3>
          <table class="product-table">
            <tr><td>Orange flavour</td><td>20 tablets</td></tr>
            <tr><td>Lemon flavour</td><td>20 tablets</td></tr>
            <tr><td>Peach flavour</td><td>10 tablets</td></tr>
            <tr><td>Apple flavour</td><td>10 tablets</td></tr>
          </table>
        </div>
      </article>

      <article class="product-block" style="top:156px">
        <div class="pack-wrap"><div class="pack" role="img" aria-label="Effervescent tube packaging reading Your Brand Here"></div><span class="count-badge">20</span></div>
        <div class="product-info">
          <h3 class="product-title">04 ZINC + VITAMIN C</h3>
          <table class="product-table">
            <tr><td>Orange flavour</td><td>20 tablets</td></tr>
            <tr><td>Berry flavour</td><td>20 tablets</td></tr>
            <tr><td>Lemon flavour</td><td>10 tablets</td></tr>
            <tr><td>Cherry flavour</td><td>10 tablets</td></tr>
          </table>
        </div>
      </article>

      <article class="product-block" style="top:290px">
        <div class="pack-wrap"><div class="pack" role="img" aria-label="Effervescent tube packaging reading Your Brand Here"></div><span class="count-badge">20</span></div>
        <div class="product-info">
          <h3 class="product-title">05 MAGNESIUM + B6 COMPLEX</h3>
          <table class="product-table">
            <tr><td>Orange flavour</td><td>20 tablets</td></tr>
            <tr><td>Lemon flavour</td><td>20 tablets</td></tr>
            <tr><td>Melon flavour</td><td>10 tablets</td></tr>
            <tr><td>Pear flavour</td><td>10 tablets</td></tr>
          </table>
        </div>
      </article>

      <svg class="page-footer" viewBox="0 0 350 44" preserveAspectRatio="none"><path d="M0 20Q175 0 350 14V44H0Z" fill="var(--blue)"/></svg>
      <span class="footer-web">www.morvaxpharma.com</span>
    </section>
  </div>

</body>
</html>
```